NEED A BUSINESS CARD FOR A NEW ELECTRICAL BUSINESS

HI I am after a new business card for my new electrical business I have a logo that I have attached its the one in blue, I would like that on the front and on the back my name- Marcus fell, Email marcusfell@tralvinet.com, mobile 0491570156, licence no# vic 48107, nsw 315042k I wont something that is a stand out from the rest but at the same time is neat as being a new business I wont it to catch peoples eye on the front of the card I would like the logo and not much else.
And on the back as well I would like a slogan saying something like
Quality-Reliable-Service

Hi all on the back of the card I would like a little slogan like Quality-Reliable-Service something like that would be good thanks

Hi all the business card needs to have both these licence numbers on it                                                  VIC-48107 nsw-315042k

```html
<!DOCTYPE html>
<html lang="en">
<head>
<meta charset="utf-8">
<title>Marcus Fell Electrical — Business Card</title>
<link rel="stylesheet" href="https://fonts.googleapis.com/css2?family=Michroma&family=Open+Sans:wght@400;600&display=swap">
<style>
  :root {
    --page-bg: #e9e7e3;
    --card-black: #0b0c0f;
    --card-black-soft: #1b1e24;
    --silver-light: #e4e6e9;
    --silver-dark: #9ea3aa;
    --blue-deep: #0c1f3d;
    --blue-mid: #173a6e;
    --blue-bright: #2f8fe0;
    --blue-soft: #3b9ae6;
    --text-white: #ffffff;
    --text-grey: #c9ced6;
    --text-dark: #2a2d33;
  }
  * { box-sizing: border-box; margin: 0; padding: 0; }
  html, body { width: 1200px; height: 1023px; overflow: hidden; }
  body {
    background: var(--page-bg);
    display: flex;
    flex-direction: column;
    align-items: center;
    justify-content: center;
    gap: 70px;
    font-family: "Open Sans", Arial, sans-serif;
  }
  .card {
    position: relative;
    width: 700px;
    height: 400px;
    border-radius: 22px;
    overflow: hidden;
  }

  /* Front */
  .card-front {
    display: grid;
    grid-template-rows: 190px 44px 1fr;
    background: var(--card-black);
  }
  .front-brand {
    background: linear-gradient(160deg, var(--card-black-soft), var(--card-black) 60%);
    display: flex;
    align-items: center;
    gap: 20px;
    padding: 0 44px;
  }
  .brand-square {
    width: 56px; height: 56px;
    background: var(--blue-bright);
    flex: none;
  }
  .brand-name {
    font-family: "Michroma", "Arial", sans-serif;
    font-size: 24px;
    letter-spacing: 1px;
    color: var(--text-white);
    line-height: 1.3;
  }
  .licence-band {
    background: linear-gradient(180deg, var(--silver-light), var(--silver-dark));
    display: flex;
    align-items: center;
    justify-content: flex-end;
    padding: 0 34px;
    font-size: 19px;
    color: var(--text-dark);
    letter-spacing: 0.5px;
  }
  .front-details {
    background: linear-gradient(135deg, var(--blue-mid), var(--blue-deep));
    display: flex;
    justify-content: space-between;
    align-items: flex-start;
    padding: 26px 34px 0 34px;
  }
  .person-name {
    font-family: "Michroma", "Arial", sans-serif;
    font-size: 26px;
    color: var(--text-white);
    letter-spacing: 1px;
  }
  .person-role {
    margin-top: 6px;
    font-size: 18px;
    color: var(--text-grey);
  }
  .contact-list { list-style: none; padding-top: 4px; }
  .contact-list li {
    display: flex;
    align-items: center;
    gap: 10px;
    font-size: 19px;
    color: var(--text-white);
    margin-bottom: 6px;
  }
  .contact-list svg { width: 16px; height: 16px; flex: none; }

  /* Back */
  .card-back {
    background: radial-gradient(ellipse at 40% 40%, var(--blue-mid), var(--blue-deep) 80%);
    display: flex;
    flex-direction: column;
    align-items: center;
    justify-content: center;
    gap: 28px;
  }
  .back-brand {
    display: flex;
    align-items: center;
    gap: 22px;
  }
  .back-brand .brand-square { width: 70px; height: 70px; background: var(--blue-soft); }
  .back-brand .brand-name { color: var(--blue-soft); font-size: 30px; }
  .slogan {
    font-family: "Michroma", "Arial", sans-serif;
    font-size: 22px;
    letter-spacing: 4px;
    color: var(--blue-soft);
  }
</style>
</head>
<body>
  <section class="card card-front" aria-label="Card front">
    <div class="front-brand">
      <span class="brand-square"></span>
      <span class="brand-name">MARCUS FELL<br>ELECTRICAL</span>
    </div>
    <div class="licence-band">VIC-48107 | NSW-315042k</div>
    <div class="front-details">
      <div class="person">
        <p class="person-name">MARCUS FELL</p>
        <p class="person-role">Director</p>
      </div>
      <ul class="contact-list">
        <li>
          <svg viewBox="0 0 16 16" aria-hidden="true"><rect width="16" height="16" rx="2" fill="#c9ced6"/><rect x="5" y="3" width="6" height="10" rx="1" fill="#173a6e"/></svg>
          0491570156
        </li>
        <li>
          <svg viewBox="0 0 16 16" aria-hidden="true"><rect width="16" height="16" rx="2" fill="#c9ced6"/><rect x="3" y="5" width="10" height="7" fill="#173a6e"/><path d="M3 5 L8 9 L13 5" stroke="#c9ced6" fill="none"/></svg>
          marcusfell@tralvinet.com
        </li>
      </ul>
    </div>
  </section>

  <section class="card card-back" aria-label="Card back">
    <div class="back-brand">
      <span class="brand-square"></span>
      <span class="brand-name">MARCUS FELL<br>ELECTRICAL</span>
    </div>
    <p class="slogan">RELIABLE / SERVICE</p>
  </section>
</body>
</html>
```